Cover for Every door Opens Where Every Door Opens

Book Cover Request
Format: Print and electronic (Quillmart)
Book Title: Every Door Opens Where Every Door Opens: Practical Roadmap for Courage and Progress
Author: R.K. Vantreel
Description: This self-help book, written by me, a self-proclaimed nobody, is filled with actionable insights and proven strategies that can help anyone. It combines humor with a serious undertone to deliver practical advice without the typical "self-helpy" vibe.
Catchphrase for the Cover: "Go from Oh Shit to Crushing It!" (or something similar)
Style: I want the cover to reflect my personality—funny, yet serious when needed. I'm open to suggestions and would love to see a design that captures the essence of the book without being too typical of the self-help genre.
Additional Information: I've attached a rough draft of the Quillmart description for more context.
Thank you for your help!
Target Market(s)
Anyone. but id say over 25
Requirements
Nice to have
- Honestly im really at a loss. Im hoping the description will help guide you. I gues i would like it to satand out of course. Be diffrent....but i know how crazy that sounds because everyone wants that. Just give me soem ideas!

```html
<!DOCTYPE html>
<html lang="en">
<head>
<meta charset="utf-8">
<title>Every Door Opens Where Every Door Opens — Book Cover</title>
<link rel="stylesheet" href="https://fonts.googleapis.com/css2?family=Bebas+Neue&family=Tinos:wght@400&display=swap">
<style>
  :root {
    --cover-dark: #161616;
    --streak-light: #2c2c2c;
    --streak-mid: #202020;
    --title-white: #ffffff;
    --band-gold: #f2b705;
    --accent-red: #d7121b;
    --sky-blue: #2f6fd6;
    --sky-light: #fdf8ec;
    --storm-grey: #6d6d6d;
    --storm-dark: #2b2b2b;
  }
  html, body {
    margin: 0;
    padding: 0;
    width: 800px;
    height: 1200px;
    overflow: hidden;
    background: var(--cover-dark);
  }
  .book-cover {
    position: relative;
    width: 800px;
    height: 1200px;
    overflow: hidden;
    background:
      repeating-linear-gradient(90deg,
        var(--streak-mid) 0px, var(--cover-dark) 2px,
        var(--streak-light) 3px, var(--cover-dark) 5px,
        var(--streak-mid) 7px, var(--cover-dark) 9px),
      var(--cover-dark);
  }
  .cover-art {
    position: absolute;
    inset: 0;
    width: 800px;
    height: 1200px;
  }
  .author-name {
    font-family: "Bebas Neue", sans-serif;
    font-size: 32px;
    letter-spacing: 9px;
    fill: var(--title-white);
  }
  .title-line {
    font-family: "Bebas Neue", sans-serif;
    fill: var(--title-white);
  }
  .title-connector {
    font-family: "Tinos", "Times New Roman", serif;
    font-size: 78px;
    fill: var(--accent-red);
  }
  .subtitle {
    font-family: "Bebas Neue", sans-serif;
    font-size: 40px;
    fill: var(--title-white);
  }
  .band-edge {
    stroke: var(--band-gold);
    stroke-width: 7;
  }
</style>
</head>
<body>
<main class="book-cover">
  <svg class="cover-art" viewBox="0 0 800 1200" xmlns="http://www.w3.org/2000/svg">
    <defs>
      <linearGradient id="sceneGradient" x1="0" y1="0" x2="1" y2="0">
        <stop offset="0" stop-color="var(--sky-blue)"/>
        <stop offset="0.33" stop-color="var(--sky-light)"/>
        <stop offset="0.45" stop-color="#f0a13a"/>
        <stop offset="0.52" stop-color="var(--storm-grey)"/>
        <stop offset="0.75" stop-color="#9a9a9a"/>
        <stop offset="1" stop-color="var(--storm-dark)"/>
      </linearGradient>
    </defs>

    <text class="author-name" x="400" y="96" text-anchor="middle">R.K. VANTREEL</text>

    <g class="title-top" transform="rotate(-7.8 400 300)">
      <text class="title-line" x="100" y="250" font-size="157" textLength="600" lengthAdjust="spacingAndGlyphs">EVERY DOOR</text>
      <text class="title-line" x="100" y="370" font-size="150" textLength="600" lengthAdjust="spacing">OPENS</text>
    </g>

    <g class="scene-band">
      <polygon points="0,437 800,327 800,740 0,847" fill="url(#sceneGradient)"
        role="img" aria-label="Photo: a man pulls back a stormy grey sky like a curtain, revealing a bright blue sky and sunlit grass"/>
      <line class="band-edge" x1="0" y1="437" x2="800" y2="327"/>
      <line class="band-edge" x1="0" y1="847" x2="800" y2="740"/>
    </g>

    <text class="title-connector" x="400" y="615" text-anchor="middle">WHERE</text>

    <g class="title-bottom" transform="rotate(-7.8 400 950)">
      <text class="title-line" x="100" y="925" font-size="157" textLength="600" lengthAdjust="spacingAndGlyphs">EVERY DOOR</text>
      <text class="title-line" x="100" y="1045" font-size="150" textLength="600" lengthAdjust="spacing">OPENS</text>
      <text class="subtitle" x="80" y="1092" textLength="640" lengthAdjust="spacingAndGlyphs">PRACTICAL ROADMAP FOR COURAGE AND PROGRESS</text>
    </g>
  </svg>
</main>
</body>
</html>
```